£500 POUND FOR A4 8 page booklet

to take 4 of my already done leaflet and make one a4 8 page booklet. The colour themes are green for fenby lodge bespoke timber frame and red for the rest. The front page needs to be the venloprime coating followed by another two pages of it www.venloprimecoating.co.uk. then two pages of fenby lodge then two pages of cadle tek then 1 page of spray protection (making sure you mention tower blocks in london )www.cadle-tek.co.uk and www.fenby-lodge.co.uk
i need the booklet to look way more professional than what these flyers are (grown up ) i can give more information ross@dunmorejoinery.com
construction

```html
<!DOCTYPE html>
<html lang="en">
<head>
<meta charset="utf-8">
<title>Cadle Tek – Booklet Spreads</title>
<link href="https://fonts.googleapis.com/css2?family=Montserrat:wght@300;400;600;700&family=Open+Sans:wght@400;600&display=swap" rel="stylesheet">
<style>
  :root{
    --bg:#d4d4d2;
    --paper:#ffffff;
    --red:#c8202a;
    --red-dark:#a5161f;
    --green:#3aa935;
    --green-soft:#b9d9b4;
    --mint:#eef3ee;
    --charcoal:#3e4441;
    --ink-light:#fde9ea;
    --photo-a:#8d7fa8;
    --photo-b:#b7b0c4;
    --photo-c:#7c5b4b;
    --photo-d:#9fb4b8;
  }
  *{box-sizing:border-box;margin:0;padding:0}
  html,body{width:898px;height:1200px;overflow:hidden;background:var(--bg)}
  body{position:relative;font-family:"Open Sans",Arial,sans-serif}
  .spread{position:absolute;left:49px;width:800px;height:566px;display:flex;box-shadow:0 6px 18px rgba(0,0,0,.18)}
  .spread--first{top:22px}
  .spread--second{top:612px}
  .page{position:relative;width:400px;height:566px;background:var(--paper);overflow:hidden}
  .page--left{border-right:1px solid #e4e4e4}
  .page__decor{position:absolute;inset:0}
  .brand{position:absolute;top:24px;left:50px;display:flex;align-items:center;gap:8px}
  .brand__dot{width:16px;height:16px;border-radius:50%;background:var(--red)}
  .brand__name{font-family:"Montserrat",Arial,sans-serif;font-weight:700;font-size:20px;color:var(--red);text-transform:uppercase;letter-spacing:1px}
  .accent-strip{position:absolute;left:10px;top:80px;width:4px;height:300px;background:var(--green)}
  .panel{position:absolute;background:var(--red);color:#fff}
  .panel--intro{left:14px;right:0;top:80px;height:300px;padding:16px 22px 0 22px}
  .panel--detail{left:0;right:0;top:232px;height:246px;padding:16px 22px}
  .eyebrow{font-family:"Montserrat",Arial,sans-serif;font-weight:300;font-size:12px;text-transform:uppercase;color:var(--ink-light);letter-spacing:.5px}
  .eyebrow b{font-weight:600;color:#fff}
  .lead{font-family:"Montserrat",Arial,sans-serif;font-weight:700;font-size:7.5px;text-transform:uppercase;line-height:1.5;margin-top:8px;letter-spacing:.2px}
  .subhead{font-family:"Montserrat",Arial,sans-serif;font-weight:600;font-size:10px;margin-top:8px}
  .columns{display:flex;gap:14px;margin-top:6px}
  .columns > div{flex:1}
  .body-text{font-size:5.6px;line-height:1.55;margin-bottom:5px;color:#fff}
  .dropcap{float:left;font-family:"Montserrat",Arial,sans-serif;font-size:22px;line-height:18px;margin-right:3px;font-weight:400}
  .col-title{font-family:"Montserrat",Arial,sans-serif;font-weight:600;font-size:7.5px;margin-bottom:5px}
  .bullets{list-style:none;margin-top:4px}
  .bullets li{font-size:5.6px;font-weight:600;margin-bottom:8px}
  .bullets li::before{content:"•";margin-right:2px}
  .photo-row{position:absolute;left:22px;right:18px;bottom:14px;height:100px;display:flex;gap:6px}
  .photo{display:block}
  .photo--a{flex:1;background:linear-gradient(135deg,var(--photo-a),var(--photo-b))}
  .photo--b{flex:1.5;background:linear-gradient(135deg,var(--photo-b),#d8d4de)}
  .photo--c{flex:.9;background:radial-gradient(circle at 50% 45%,#e29a42,#9b2020 70%)}
  .photo--d{flex:1;background:linear-gradient(135deg,#5f9aa5,var(--photo-d))}
  .photo--e{flex:1.5;background:linear-gradient(180deg,#b9c3c7,#c5a46a)}
  .photo--f{flex:.9;background:linear-gradient(160deg,#1d2f55,#5c6f96)}
  .dark-block{position:absolute;left:30px;right:0;top:22px;height:150px;background:var(--charcoal)}
  .hero-photo{position:absolute;left:22px;right:24px;top:64px;height:200px}
  .hero-photo--air{background:linear-gradient(120deg,#8a6a45,#a79bc2 45%,#d9d4dc 80%)}
  .hero-photo--film{background:linear-gradient(120deg,#8fb0b8,#b6d0d3 50%,#7b3f3a 85%)}
  .page-number{position:absolute;font-family:"Montserrat",Arial,sans-serif;font-weight:700;font-size:20px}
  .page-number--left{left:40px;top:400px;color:var(--green-soft)}
  .page-number--right{right:40px;bottom:36px;color:var(--red)}
  .partner{position:absolute;left:150px;top:462px;display:flex;align-items:center;gap:7px}
  .partner__mark{width:14px;height:14px;background:var(--green)}
  .partner__mark--blue{background:#1e4f9c}
  .partner__name{font-family:"Montserrat",Arial,sans-serif;font-weight:700;font-size:16px;text-transform:uppercase}
  .partner__name--green{color:var(--green)}
  .partner__name--blue{color:#1e4f9c}
</style>
</head>
<body>

<!-- Spread: pages 05–06 -->
<section class="spread spread--first">
  <article class="page page--left">
    <svg class="page__decor" viewBox="0 0 400 566" aria-hidden="true"><polygon points="250,0 400,0 400,220" fill="var(--mint)"/><polygon points="80,566 400,330 400,566" fill="var(--mint)"/></svg>
    <div class="brand"><span class="brand__dot"></span><span class="brand__name">cadle tek</span></div>
    <div class="accent-strip"></div>
    <div class="panel panel--intro">
      <p class="eyebrow">About <b>Cadle Tek</b></p>
      <p class="lead">Cadle Tek is a primarily family run company that is part of a group of companies that has dominated the construction industry for the last decade.</p>
      <p class="subhead">Air Testing Specialists</p>
      <div class="columns">
        <div><p class="body-text"><span class="dropcap">C</span>adle Tek operates to accredited standards across the UK. Our trained engineers are fully certified and work with every major site contractor.</p></div>
        <div><p class="body-text">Sealcore is a high performance spray foam system for walls, floors and roofs that gives an airtight seal and lasting thermal comfort.</p></div>
      </div>
      <div class="photo-row">
        <span class="photo photo--a" role="img" aria-label="Operative spraying insulation foam onto a wall"></span>
        <span class="photo photo--b" role="img" aria-label="Spray foam insulation between roof rafters"></span>
        <span class="photo photo--c" role="img" aria-label="Air testing fan fitted in a doorway"></span>
      </div>
    </div>
    <span class="page-number page-number--left">05</span>
    <div class="partner"><span class="partner__mark"></span><span class="partner__name partner__name--green">Sealcore</span></div>
  </article>

  <article class="page page--right">
    <svg class="page__decor" viewBox="0 0 400 566" aria-hidden="true"><polygon points="0,566 0,420 240,566" fill="var(--mint)"/></svg>
    <div class="dark-block"></div>
    <div class="hero-photo hero-photo--air" role="img" aria-label="Operative in protective suit spraying foam insulation under roof timbers"></div>
    <div class="panel panel--detail">
      <div class="columns">
        <div>
          <p class="eyebrow">Air <b>Testing</b></p>
          <p class="body-text" style="margin-top:6px"><span class="dropcap">O</span>nsite testing with same day certification. This also includes building calculation and full reports on our test.</p>
          <p class="body-text">Airtightness plays a significant role in the energy efficiency of buildings. By limiting the leakage of heated air we reduce energy use and costs.</p>
          <p class="body-text">The government has made commitments to reduce carbon emissions through the European Energy Performance of Buildings Directive and the Kyoto Agreement.</p>
        </div>
        <div style="padding-top:22px">
          <p class="col-title">What we offer:</p>
          <p class="body-text">Smoke Pen Testing: On site testing which will highlight areas of leakage in the building that need attention prior to air testing.</p>
          <p class="body-text">Air Permeability: Air permeability is the control of air leakage through the fabric of the building. This will include both pressurisation and ventilation measurement of the building.</p>
        </div>
      </div>
    </div>
    <span class="page-number page-number--right">06</span>
  </article>
</section>

<!-- Spread: pages 07–08 -->
<section class="spread spread--second">
  <article class="page page--left">
    <svg class="page__decor" viewBox="0 0 400 566" aria-hidden="true"><polygon points="250,0 400,0 400,220" fill="var(--mint)"/><polygon points="80,566 400,330 400,566" fill="var(--mint)"/></svg>
    <div class="brand"><span class="brand__dot"></span><span class="brand__name">cadle tek</span></div>
    <div class="accent-strip"></div>
    <div class="panel panel--intro">
      <p class="eyebrow">About <b>Spray Protection</b></p>
      <p class="lead">Sprayed film as protection of the outside of the windows during facade renovation works</p>
      <p class="subhead">Peelsafe Spray Protection</p>
      <div class="columns">
        <div>
          <p class="body-text"><span class="dropcap">A</span>pplication is sprayed directly to a durable, transparent protective film. The film protects the glass and frames against damage from works nearby.</p>
          <p class="body-text">Peelsafe protects against damage caused by plaster and concrete splashes, grinding sparks and paint.</p>
        </div>
        <div>
          <p class="body-text">Peelsafe can be applied on glass, windows with PVC and aluminium profiles, tower blocks in London and other sites.</p>
          <p class="body-text">By leaving Peelsafe on the windows slightly open, the ventilation can be kept during works without damaging film.</p>
        </div>
      </div>
      <div class="photo-row">
        <span class="photo photo--d" role="img" aria-label="Operative spraying protective film onto glazing"></span>
        <span class="photo photo--e" role="img" aria-label="Building facade with protected windows on site"></span>
        <span class="photo photo--f" role="img" aria-label="Operative peeling protective film from a window"></span>
      </div>
    </div>
    <span class="page-number page-number--left">07</span>
    <div class="partner"><span class="partner__mark partner__mark--blue"></span><span class="partner__name partner__name--blue">Peelsafe</span></div>
  </article>

  <article class="page page--right">
    <svg class="page__decor" viewBox="0 0 400 566" aria-hidden="true"><polygon points="0,566 0,420 240,566" fill="var(--mint)"/></svg>
    <div class="dark-block"></div>
    <div class="hero-photo hero-photo--film" role="img" aria-label="Operative removing protective film from a window frame"></div>
    <div class="panel panel--detail">
      <div class="columns">
        <div>
          <p class="eyebrow">What do <b>we do ?</b></p>
          <p class="body-text" style="margin-top:6px">Cadle Tek spray apply a special formula on site:</p>
          <ul class="bullets">
            <li>Windows and frames</li>
            <li>Sanitary ware</li>
            <li>Polished concrete</li>
            <li>New or existing Facades</li>
          </ul>
        </div>
        <div style="padding-top:40px">
          <p class="body-text">This protects the covered items from scratches and general damage caused on active building sites. Peelsafe can be left for up to two years before it has to be removed.</p>
        </div>
      </div>
    </div>
    <span class="page-number page-number--right">08</span>
  </article>
</section>

</body>
</html>
```